Cyber Security firm requires new branding and website design

We are open to advice on project budget so feel free to message me regarding this. We understand there are people from all over the world looking at this so initially we may be looking at just a landing page to just give us an idea of the design and that can be enough to win this contest. From there we can agree a reward / payment for the whole site.
We're looking for a Designer with UI/UX and some branding skills. We really need someone to give us a direction and then create a mock-up in Photoshop. We have a great logo and so far our website has done the job but is very basic www.vandrelock.com . We can reuse most the content (and this can be used by the Designer) but we need a complete redesign. Keep it clear, simple, classy and uncluttered and we certainly need new color scheme.
I have attached our logo's and a copy of our business cards (the black logo is actually silver foil) to give you an idea of the sort of branding we like.
We are based in Los Angeles and our clients range from the Entertainment business and start-ups to Law and Financial firms so we need a site design that appeals to all of these sectors.
Once we have the design we can give it to our developer to turn into a working site.
Updates
I wasn't sure how this worked as its the first time I have used the site.
Happy to take feedback on what would be most attractive to you guys to get you to want to design for us.
Cheers
Tomas
The styles we like personally tend to have blocks of content and some funky HTML 5 stuff (If you can design it we can code it). Here are some examples:
http://www.plumo.co
http://quillbendpilates.com/
http://harborweave.com/
We are a fun company and have a good sense of humor. Our client generally do too but they are also dealing with serious issues so if you can get something that's fun but puts across that we are serious about what we do that would be great. Oh and we love this one so if you can take some influence from this but keep it professional we would love to see it:
http://mildcometworks.com/
I also like the old typewriter style lettering i have seen used on contact forms. However this has to be a cohesive design so we want you to add what looks right not just everything we like (unless you can do that well).
We understand that you show a static site so this is hard to demonstrate but we particularly like the videos people are embedding nowadays and would love to avoid stock photos where we can:
https://www.coinvesta.com/home
Hopefully this gives you all more food for thought.
Industry/Entity Type
Business
Colors
Designer to choose colors to be used in the design.
Look and feel
Each slider illustrates characteristics of the customer's brand and the style your logo design should communicate.

```html
<!DOCTYPE html>
<html lang="en">
<head>
<meta charset="utf-8">
<title>Vandrelock Security</title>
<link href="https://fonts.googleapis.com/css2?family=Open+Sans:wght@300;400;600;700&display=swap" rel="stylesheet">
<style>
:root{
  --navy:#1f2c39;
  --navy-deep:#17222d;
  --navy-card:#263646;
  --teal:#19b5a5;
  --ink:#3d4650;
  --muted:#7c8690;
  --line:#d6dadd;
  --paper:#ffffff;
  --mist:#f3f4f5;
}
*{box-sizing:border-box;margin:0;padding:0}
html,body{width:1200px;height:4068px;overflow:hidden}
body{font-family:"Open Sans",Arial,sans-serif;color:var(--ink);background:var(--paper);position:relative;font-size:13px}
.btn{display:inline-block;background:var(--teal);color:#fff;font-size:11px;font-weight:600;padding:7px 16px;border-radius:2px}
.section-title{position:absolute;left:0;width:1200px;text-align:center;font-size:20px;font-weight:400}
.rule-title{display:flex;align-items:center;justify-content:center;gap:18px}
.rule-title::before,.rule-title::after{content:"";width:260px;height:1px;background:var(--line)}
.lede{position:absolute;left:350px;width:500px;text-align:center;font-size:14px;line-height:20px}
.zig{position:absolute;left:0;width:1200px;height:10px}

/* header */
.site-header{position:absolute;top:0;left:0;width:1200px;height:51px;background:#fff;border-bottom:1px solid var(--line)}
.brand{position:absolute;left:244px;top:8px;display:flex;align-items:center;gap:8px;color:var(--navy)}
.brand-mark{width:30px;height:30px;border:3px solid var(--navy);flex:none}
.brand-name{font-weight:700;font-size:14px;line-height:15px;letter-spacing:1px}
.main-nav{position:absolute;left:506px;top:0;display:flex;gap:26px;font-size:12px;color:var(--muted)}
.main-nav a{padding-top:18px;height:51px;color:inherit;text-decoration:none}
.main-nav a.active{color:var(--teal);border-top:3px solid var(--teal);padding-top:15px}

/* hero */
.hero{position:absolute;top:51px;left:0;width:1200px;height:356px;background:linear-gradient(180deg,#22313f,#1c2835)}
.hero-panel{position:absolute;left:288px;top:176px;width:627px;height:316px;background:var(--navy);border:4px solid #fff;box-shadow:0 4px 14px rgba(0,0,0,.25);padding:60px 40px}
.hero-panel h1{color:var(--teal);font-weight:300;font-size:23px;margin-bottom:28px;white-space:nowrap}
.hero-panel p{color:#8d99a5;font-size:13px;line-height:19px;width:330px;margin-bottom:28px}
.arrow{position:absolute;top:312px;width:40px;height:40px;border-radius:50%;background:#fff;box-shadow:0 2px 6px rgba(0,0,0,.3)}
.arrow svg{position:absolute;left:13px;top:12px}
.dots{position:absolute;left:0;width:1200px;display:flex;justify-content:center;gap:10px}
.dots i{width:16px;height:16px;border-radius:50%;border:2px solid #9aa4ad}
.dots i.on{background:var(--teal);border-color:var(--teal)}

/* services */
.services{position:absolute;top:680px;left:0;width:1200px;height:388px;background:var(--navy)}
.services .section-title{color:#fff;top:22px}
.services .underline{position:absolute;left:400px;top:58px;width:400px;height:1px;background:#3d4e5f}
.service-card{position:absolute;top:117px;width:214px;height:193px;background:var(--navy-deep);text-align:center;padding-top:30px}
.service-card .icon{position:absolute;left:82px;top:-26px;width:50px;height:50px;border-radius:50%;background:var(--teal);border:4px solid var(--navy-deep)}
.service-card h3{color:#fff;font-size:14px;font-weight:600;margin-bottom:10px}
.service-card p{color:#aab4bd;font-size:10px;line-height:14px;padding:0 16px;text-align:left;margin-bottom:14px}
.services .note{position:absolute;top:322px;left:0;width:1200px;text-align:center;color:#fff;font-size:14px}
.services .note-btn{position:absolute;top:350px;left:540px;width:120px;text-align:center;background:#fff;color:var(--navy);font-size:11px;padding:6px 0}

/* team */
.team{position:absolute;top:1068px;left:0;width:1200px;height:1252px;background:var(--mist)}
.member{position:absolute;top:261px;width:214px;height:318px;background:#fff;box-shadow:0 1px 3px rgba(0,0,0,.12)}
.member .photo{width:214px;height:207px;background:linear-gradient(160deg,#8aa0b4,#4d5d6b)}
.member .meta{padding:8px 10px 0;font-size:10px;line-height:13px;color:var(--muted)}
.member .meta b{display:block;color:var(--ink);font-size:11px}
.member .meta em{display:block;font-style:normal;color:var(--teal);margin-bottom:6px;padding-bottom:4px;border-bottom:1px solid var(--line)}
.member .btn{position:absolute;left:75px;bottom:-12px}
.team .tagline{position:absolute;top:677px;left:350px;width:500px;text-align:center;color:var(--teal);font-size:14px;line-height:20px;border-top:1px solid var(--line);border-bottom:1px solid var(--line);padding:14px 0}
.column{position:absolute;top:797px;width:214px}
.column h3{font-size:17px;font-weight:400;padding-bottom:10px;border-bottom:2px solid var(--teal);margin-bottom:14px}
.column p{font-size:10px;line-height:14px;color:var(--muted);margin-bottom:12px}
.cta-bar{position:absolute;top:1165px;left:339px;width:519px;height:58px;background:var(--navy);display:flex;align-items:center;justify-content:space-around;color:#fff;font-size:13px;font-weight:600}
.cta-bar .btn{background:#fff;color:var(--navy);font-weight:400}

/* clients */
.clients-head{position:absolute;top:2320px;left:0;width:1200px;height:148px;background:#fff}
.testimonial{position:absolute;top:2468px;left:0;width:1200px;height:335px;background:var(--navy);color:#fff}
.avatar{position:absolute;left:540px;top:57px;width:120px;height:120px;border-radius:50%;border:5px solid #fff;background:linear-gradient(160deg,#c9ced3,#6d7883)}
.quote{position:absolute;top:200px;left:300px;width:600px;text-align:center;font-size:14px;line-height:21px;font-weight:600}
.quote span{display:block;text-align:right;font-size:12px;font-weight:400}
.logo-grid{position:absolute;top:2830px;left:322px;width:559px;height:208px;display:grid;grid-template-columns:repeat(4,1fr);grid-template-rows:1fr 1fr}
.logo-grid div{display:flex;align-items:center;justify-content:center;gap:8px;font-weight:700;font-size:17px;color:#8a949c;border-right:1px solid var(--line);border-bottom:1px solid var(--line)}
.logo-grid div:nth-child(4n){border-right:0}
.logo-grid div:nth-child(n+5){border-bottom:0}
.logo-grid .tint{color:var(--teal)}
.logo-grid i{width:10px;height:10px;background:currentColor;border-radius:50%}

.quote-band{position:absolute;top:3119px;left:0;width:1200px;height:186px;background:var(--navy)}
.quote-band p{position:absolute;top:40px;left:380px;width:440px;text-align:center;color:var(--teal);font-size:14px;line-height:20px}
.quote-band .rule{position:absolute;top:112px;left:460px;width:280px;height:1px;background:#4d5e6e}

/* stats */
.stats{position:absolute;top:3370px;left:0;width:1200px;height:130px;border-top:1px solid var(--line);border-bottom:1px solid var(--line);background:#fff}
.stat{position:absolute;top:40px;display:flex;align-items:center;gap:12px}
.stat b{display:block;font-size:26px;font-weight:400;color:var(--ink);line-height:28px}
.stat small{font-size:9px;color:var(--muted)}

.social-band{position:absolute;top:3520px;left:0;width:1200px;height:110px;background:var(--teal);color:#fff;font-size:11px}
.social-band .handle{position:absolute;left:340px;top:38px;display:flex;align-items:center;gap:10px}
.social-band .handle i{width:22px;height:22px;border-radius:50%;background:#fff}
.social-band .tweet{position:absolute;left:500px;top:43px}
.social-band .more{position:absolute;left:0;width:1200px;top:78px;text-align:center;font-size:9px}

/* contact */
.contact{position:absolute;top:3630px;left:0;width:1200px;height:388px;background:var(--navy);color:#fff}
.contact .section-title{top:26px}
.contact .rule-title::before,.contact .rule-title::after{background:#3d4e5f}
.contact .lede{top:66px;color:#c7cfd6}
.form{position:absolute;left:244px;top:155px;width:383px}
.field{background:var(--navy-card);height:26px;font-size:10px;color:#8795a2;padding:6px 8px;margin-bottom:10px}
.field.half{display:inline-block;width:184px}
.field.half+.field.half{margin-left:11px}
.field.area{height:132px}
.info{position:absolute;left:660px;top:155px;width:290px;font-size:10px}
.info-row{display:flex;align-items:flex-start;margin-bottom:18px}
.info-row i{width:22px;height:22px;border-radius:50%;background:var(--teal);margin-right:10px;flex:none}
.info-row .label{width:90px;color:#fff;padding-top:4px}
.info-row .val{color:#aab4bd;line-height:14px;padding-top:4px}

.site-footer{position:absolute;top:4018px;left:0;width:1200px;height:50px;background:var(--navy-deep);color:#8795a2;font-size:10px}
.site-footer .copy{position:absolute;left:244px;top:18px}
.site-footer .socials{position:absolute;left:690px;top:18px;display:flex;gap:10px}
.site-footer .socials i{width:12px;height:12px;background:#8795a2;border-radius:2px}
.to-top{position:absolute;left:912px;top:8px;width:42px;height:42px;background:var(--teal)}
</style>
</head>
<body>

<header class="site-header">
  <div class="brand"><span class="brand-mark"></span><span class="brand-name">VANDRELOCK<br>SECURITY</span></div>
  <nav class="main-nav">
    <a class="active">Home</a><a>Penetration Testing</a><a>Staffing</a><a>News</a><a>About Us</a><a>Contact Us</a>
  </nav>
</header>

<section class="hero" role="img" aria-label="Dark backdrop with a faint pattern of technology icons"></section>
<svg class="zig" style="top:402px" viewBox="0 0 1200 10" preserveAspectRatio="none"><path d="M0 0H1200V5L1195 10 1190 5 1185 10 1180 5 1175 10 1170 5 1165 10 1160 5 1155 10 1150 5 1145 10 1140 5 1135 10 1130 5 1125 10 1120 5 1115 10 1110 5 1105 10 1100 5 1095 10 1090 5 1085 10 1080 5 1075 10 1070 5 1065 10 1060 5 1055 10 1050 5 1045 10 1040 5 1035 10 1030 5 1025 10 1020 5 1015 10 1010 5 1005 10 1000 5 995 10 990 5 985 10 980 5 975 10 970 5 965 10 960 5 955 10 950 5 945 10 940 5 935 10 930 5 925 10 920 5 915 10 910 5 905 10 900 5 895 10 890 5 885 10 880 5 875 10 870 5 865 10 860 5 855 10 850 5 845 10 840 5 835 10 830 5 825 10 820 5 815 10 810 5 805 10 800 5 795 10 790 5 785 10 780 5 775 10 770 5 765 10 760 5 755 10 750 5 745 10 740 5 735 10 730 5 725 10 720 5 715 10 710 5 705 10 700 5 695 10 690 5 685 10 680 5 675 10 670 5 665 10 660 5 655 10 650 5 645 10 640 5 635 10 630 5 625 10 620 5 615 10 610 5 605 10 600 5 595 10 590 5 585 10 580 5 575 10 570 5 565 10 560 5 555 10 550 5 545 10 540 5 535 10 530 5 525 10 520 5 515 10 510 5 505 10 500 5 495 10 490 5 485 10 480 5 475 10 470 5 465 10 460 5 455 10 450 5 445 10 440 5 435 10 430 5 425 10 420 5 415 10 410 5 405 10 400 5 395 10 390 5 385 10 380 5 375 10 370 5 365 10 360 5 355 10 350 5 345 10 340 5 335 10 330 5 325 10 320 5 315 10 310 5 305 10 300 5 295 10 290 5 285 10 280 5 275 10 270 5 265 10 260 5 255 10 250 5 245 10 240 5 235 10 230 5 225 10 220 5 215 10 210 5 205 10 200 5 195 10 190 5 185 10 180 5 175 10 170 5 165 10 160 5 155 10 150 5 145 10 140 5 135 10 130 5 125 10 120 5 115 10 110 5 105 10 100 5 95 10 90 5 85 10 80 5 75 10 70 5 65 10 60 5 55 10 50 5 45 10 40 5 35 10 30 5 25 10 20 5 15 10 10 5 5 10 0 5Z" fill="#1c2835"/></svg>

<div class="hero-panel">
  <h1>Dedicated to your infosec staffing requirements</h1>
  <p>Vandrelock Security is a boutique company that is devoted to infosec resourcing, with qualified, in-house security professionals that help teams.</p>
  <span class="btn">Contact Us</span>
</div>
<div class="arrow" style="left:245px"><svg width="14" height="16" viewBox="0 0 14 16"><path d="M10 2 4 8l6 6" stroke="#1f2c39" stroke-width="3" fill="none"/></svg></div>
<div class="arrow" style="left:916px"><svg width="14" height="16" viewBox="0 0 14 16"><path d="M4 2l6 6-6 6" stroke="#1f2c39" stroke-width="3" fill="none"/></svg></div>
<div class="dots" style="top:521px"><i></i><i class="on"></i><i></i></div>
<p class="lede" style="top:572px">Donec sollicitudin molestie malesuada. Nulla quis lorem ut libero mal suada feugiat. Curabitur aliquet quam id lorem</p>

<section class="services">
  <h2 class="section-title">Our Services</h2>
  <div class="underline"></div>
  <div class="service-card" style="left:244px"><span class="icon"></span><h3>Securities</h3><p>Donec sollicitudin molestie malesuada. Curabitur aliquet quam id dui posuere blandit. Donec sollicitudin molestie, vivamus magna justo lacinia eget.</p><span class="btn">Learn More</span></div>
  <div class="service-card" style="left:492px"><span class="icon"></span><h3>Consulting</h3><p>Donec sollicitudin molestie malesuada. Curabitur aliquet quam id dui posuere blandit. Donec sollicitudin molestie, vivamus magna justo lacinia eget.</p><span class="btn">Learn More</span></div>
  <div class="service-card" style="left:739px"><span class="icon"></span><h3>Projects</h3><p>Donec sollicitudin molestie malesuada. Curabitur aliquet quam id dui posuere blandit. Donec sollicitudin molestie, vivamus magna justo lacinia eget.</p><span class="btn">Learn More</span></div>
  <p class="note">Contact us if you have any special requirements</p>
  <span class="note-btn">Contact Us</span>
</section>

<section class="team">
  <h2 class="section-title rule-title" style="top:38px">About Us</h2>
  <p class="lede" style="top:96px">Donec sollicitudin molestie malesuada. Nulla quis lorem ut libero mal suada feugiat. Curabitur aliquet quam id lorem</p>
  <div class="member" style="left:244px"><div class="photo" role="img" aria-label="Portrait photo of a team member"></div><div class="meta"><b>Mr. Tomas Crane</b><em>Founder</em>Donec sollicitudin molestie malesuada. Curabitur aliquet quam id dui posuere blandit. Donec sollicitudin.</div><span class="btn">Get Hire</span></div>
  <div class="member" style="left:492px"><div class="photo" role="img" aria-label="Portrait photo of a team member"></div><div class="meta"><b>Mr. Peter Harlow</b><em>Director</em>Donec sollicitudin molestie malesuada. Curabitur aliquet quam id dui posuere blandit. Donec sollicitudin.</div><span class="btn">Get Hire</span></div>
  <div class="member" style="left:739px"><div class="photo" role="img" aria-label="Portrait photo of a team member"></div><div class="meta"><b>Mrs. Anna Roswell</b><em>Manager</em>Donec sollicitudin molestie malesuada. Curabitur aliquet quam id dui posuere blandit. Donec sollicitudin.</div><span class="btn">Get Hire</span></div>
  <p class="tagline">Donec sollicitudin molestie malesuada. Nulla quis lorem ut libero mal suada feugiat. Curabitur aliquet quam id lorem</p>
  <div class="column" style="left:244px"><h3>About Us</h3><p>Donec sollicitudin molestie malesuada. Curabitur aliquet quam id dui posuere blandit. Donec sollicitudin molestie malesuada. Lorem ipsum dolor sit amet, consectetur adipiscing elit. Cras ultricies ligula sed magna dictum porta.</p><p>Vivamus suscipit tortor eget felis porttitor volutpat. Nulla porttitor accumsan tincidunt. Curabitur non nulla sit amet nisl tempus convallis quis ac lectus. Pellentesque in ipsum id orci porta dapibus.</p></div>
  <div class="column" style="left:492px"><h3>Our Missions</h3><p>Donec sollicitudin molestie malesuada. Curabitur aliquet quam id dui posuere blandit. Donec sollicitudin molestie malesuada. Lorem ipsum dolor sit amet, consectetur adipiscing elit. Cras ultricies ligula sed magna dictum porta.</p><p>Vivamus suscipit tortor eget felis porttitor volutpat. Nulla porttitor accumsan tincidunt.</p></div>
  <div class="column" style="left:739px"><h3>Our Vision</h3><p>Donec sollicitudin molestie malesuada. Curabitur aliquet quam id dui posuere blandit. Donec sollicitudin molestie malesuada. Lorem ipsum dolor sit amet, consectetur adipiscing elit.</p><p>Cras ultricies ligula sed magna dictum porta. Vivamus suscipit tortor eget felis porttitor volutpat. Nulla porttitor accumsan tincidunt.</p></div>
  <div class="cta-bar">Donec sollicitudin molestie malesuada nulla <span class="btn">Reach Out Now</span></div>
</section>

<section class="clients-head">
  <h2 class="section-title rule-title" style="top:18px">Clients</h2>
  <p class="lede" style="top:66px">Donec sollicitudin molestie malesuada. Nulla quis lorem ut libero mal suada feugiat. Curabitur aliquet quam id lorem</p>
</section>
<section class="testimonial">
  <div class="avatar" role="img" aria-label="Round portrait photo of a client"></div>
  <p class="quote">Donec sollicitudin molestie malesuada. Curabitur aliquet quam id dui posuere sit. Sollicitudin lorem molestie malesuada. Lorem ipsum dolor sit amet, consectetur.<span>- Lorenzo, CEO</span></p>
  <div class="dots" style="top:294px"><i></i><i class="on"></i><i></i></div>
</section>

<div class="logo-grid">
  <div class="tint"><i></i>Halfmoon</div><div>Orbitline</div><div><i></i>Launchpad</div><div><i></i>Redfield</div>
  <div><i></i>Lunaris</div><div><i></i>Redfield</div><div class="tint">Halfmoon</div><div>Orbitline</div>
</div>

<section class="quote-band">
  <p>Donec sollicitudin molestie malesuada. Nulla quis lorem ut libero malesuada feugiat. Curabitur aliquet quam id lorem</p>
  <div class="rule"></div>
  <div class="dots" style="top:136px"><i></i><i class="on"></i><i></i></div>
</section>

<section class="stats">
  <div class="stat" style="left:244px"><svg width="44" height="44" viewBox="0 0 44 44"><circle cx="22" cy="12" r="10" fill="#19b5a5"/><path d="M2 44c0-14 9-20 20-20s20 6 20 20Z" fill="#19b5a5"/></svg><div><b>230</b><small>Customers</small></div></div>
  <div class="stat" style="left:440px"><svg width="48" height="44" viewBox="0 0 48 44"><path d="M24 44 4 24C-4 14 4 0 14 2c5 1 8 4 10 7 2-3 5-6 10-7 10-2 18 12 10 22Z" fill="#19b5a5"/></svg><div><b>12</b><small>Awards</small></div></div>
  <div class="stat" style="left:630px"><svg width="44" height="48" viewBox="0 0 44 48"><rect x="17" y="0" width="10" height="5" fill="#19b5a5"/><circle cx="22" cy="27" r="18" fill="none" stroke="#19b5a5" stroke-width="5"/><path d="M22 27V16" stroke="#19b5a5" stroke-width="4"/></svg><div><b>2380</b><small>Completed Projects</small></div></div>
  <div class="stat" style="left:810px"><svg width="44" height="44" viewBox="0 0 44 44"><circle cx="22" cy="22" r="20" fill="#19b5a5"/></svg><div><b>50890</b><small>Followers</small></div></div>
</section>

<section class="social-band">
  <div class="handle"><i></i>@vandrelock</div>
  <div class="tweet">Donec sollicitudin molestie malesuada nulla quis lorem ut libero</div>
  <div class="more">Follow us for updates</div>
</section>

<section class="contact">
  <h2 class="section-title rule-title">Contact Us</h2>
  <p class="lede">Donec sollicitudin molestie malesuada. Nulla quis lorem ut libero mal suada feugiat. Curabitur aliquet quam id lorem</p>
  <div class="form">
    <div class="field half">Name</div><div class="field half">Mail</div>
    <div class="field area">Message</div>
    <span class="btn">Send Message</span>
  </div>
  <div class="info">
    <div class="info-row"><i></i><span class="label">Our Home</span><span class="val">218 Larkspur Row<br>Marlow Heights, CA 90000</span></div>
    <div class="info-row"><i></i><span class="label">Call Us</span><span class="val">(555) 010-2468</span></div>
    <div class="info-row"><i></i><span class="label">Opening Time</span><span class="val">Mon - Fri: 9 - 6<br>Sat: 10 - 4<br>Sun: Closed</span></div>
  </div>
</section>

<footer class="site-footer">
  <span class="copy">© Copyright 2014. All Rights Reserved.</span>
  <div class="socials"><i></i><i></i><i></i><i></i><i></i><i></i><i></i></div>
  <span class="to-top"><svg width="42" height="42" viewBox="0 0 42 42"><path d="M14 24l7-7 7 7" stroke="#fff" stroke-width="3" fill="none"/></svg></span>
</footer>

</body>
</html>
```